International Business Consulting Company Website

RK Harbor Advisors is a U.S-based international consulting firm. We combined passion for success in the global business arena with hands-on experience to help foreign companies navigate the entry into U.S. markets and U.S. companies in initiating and expanding exports to foreign markets.

We need a simple 1 page website
Examples of other consultants’ websites:
http://www.brindlemarkgroup.example/#intro
https://www.tpq-advisory.example
http://morivetagroup.example
https://quillstoneadvisors.example

I also need the designer to suggest stock images that are suitable (related to international business, exports).

We want our web design to be bold, yet clean and simple.

Target Market(s)

US companies that export abroad, foreign companies that want to do business int he US/ open a subsidiary in the US.

Industry/Entity Type

Business Consultant

Coding

Coded - Design and coding required

Font styles to use
Sans Serif

Requirements
Must have
• Company logo on top

```html
<!DOCTYPE html>
<html lang="en">
<head>
<meta charset="utf-8">
<title>RK Harbor Advisors</title>
<link rel="stylesheet" href="https://fonts.googleapis.com/css2?family=Montserrat:wght@400;500&family=Raleway:wght@500;600&family=Roboto:wght@400&display=swap">
<style>
  :root {
    --header-bg: #1b1b1b;
    --white: #ffffff;
    --ink: #111111;
    --body-text: #333333;
    --hero-deep: #1e3350;
    --hero-mid: #4f6f98;
    --hero-light: #9fb6d4;
  }
  * { box-sizing: border-box; margin: 0; padding: 0; }
  html, body { width: 1200px; height: 973px; overflow: hidden; background: var(--white); }
  body { font-family: "Montserrat", sans-serif; }

  .site-header {
    height: 78px;
    background: var(--header-bg);
    display: flex;
    align-items: center;
    justify-content: space-between;
    padding: 0 106px 0 127px;
  }
  .brand { display: flex; align-items: center; gap: 8px; color: var(--white); text-decoration: none; }
  .brand-square { width: 43px; height: 43px; border: 2px solid var(--white); }
  .brand-name { font-family: "Montserrat", sans-serif; font-weight: 500; font-size: 17px; letter-spacing: 1px; text-transform: uppercase; }

  .main-nav { display: flex; align-items: center; gap: 24px; }
  .main-nav a { color: var(--white); text-decoration: none; font-size: 14px; font-weight: 500; letter-spacing: 0.8px; }
  .search-icon { width: 17px; height: 17px; margin-left: 0; }

  .hero {
    position: relative;
    height: 605px;
    background:
      radial-gradient(ellipse at 70% 55%, rgba(190,210,235,0.55), transparent 55%),
      linear-gradient(180deg, var(--hero-light) 0%, var(--hero-mid) 45%, var(--hero-deep) 100%);
    display: flex;
    flex-direction: column;
    align-items: center;
    color: var(--white);
    text-align: center;
  }
  .hero-title { font-family: "Raleway", sans-serif; font-weight: 600; font-size: 41px; margin-top: 297px; letter-spacing: 0.5px; }
  .hero-tagline { font-family: "Raleway", sans-serif; font-weight: 600; font-size: 18px; margin-top: 18px; }
  .hero-button {
    margin-top: 22px;
    width: 184px; height: 40px;
    border: 1px solid rgba(255,255,255,0.6);
    color: var(--white); text-decoration: none;
    font-family: "Montserrat", sans-serif; font-size: 16px; letter-spacing: 2.5px;
    display: flex; align-items: center; justify-content: center;
  }

  .welcome { text-align: center; padding: 0 127px; }
  .welcome-title { font-weight: 400; font-size: 32px; color: var(--ink); margin-top: 122px; letter-spacing: 0.5px; }
  .welcome-text { font-family: "Roboto", sans-serif; font-size: 13px; color: var(--body-text); line-height: 24px; letter-spacing: 0.6px; margin-top: 22px; }
</style>
</head>
<body>
  <header class="site-header">
    <a class="brand" href="#">
      <span class="brand-square"></span>
      <span class="brand-name">RK Harbor Advisors</span>
    </a>
    <nav class="main-nav">
      <a href="#">HOME</a>
      <a href="#">OUR SERVICES</a>
      <a href="#">ABOUT</a>
      <a href="#">CONTACT</a>
      <svg class="search-icon" viewBox="0 0 17 17" aria-label="Search">
        <circle cx="10" cy="7" r="5.5" fill="none" stroke="#fff" stroke-width="1.6"/>
        <line x1="6" y1="11" x2="1.5" y2="15.5" stroke="#fff" stroke-width="1.8" stroke-linecap="round"/>
      </svg>
    </nav>
  </header>

  <section class="hero" role="img" aria-label="Businessman on a phone in front of a night city skyline with glass towers, in blue tones">
    <h1 class="hero-title">RK HARBOR ADVISORS</h1>
    <p class="hero-tagline">~ Global Exports ~ Market Entry &amp; Site Selection in the U.S.</p>
    <a class="hero-button" href="#">LEARN MORE</a>
  </section>

  <section class="welcome">
    <h2 class="welcome-title">WELCOME RK HARBOR ADVISORS</h2>
    <p class="welcome-text">RK Harbor Advisors is a U.S-based international consulting firm. We combined passion for success in the global business arena with hands-on experience to help foreign companies navigate the entry into U.S. markets and U.S. companies in initiating and expanding exports to foreign markets.</p>
  </section>
</body>
</html>
```